Our Chalet for rent needs a new website

Hi guys we have a chalet for rent and we finally want to have our own website for information and bookings the information is posted below and will upload pictures in due course.

Thanks

Chalet | 5 bedrooms | sleeps 11

Key Info
Beach or lakeside relaxationSkiGreat for children of all agesSome pets are welcome - please contact the ownerPrivate gardenCar advised
Exceptionally renovated Fern Byre dates from 1781 and offers the discerning skier a chance to stay in a wonderful mountain lodge. Spacious and light, there is a superb double aspect living and dining area and open-plan kitchen. All bedrooms are ensuite,and facilities include a sauna, enormous 6m 'Swim spa' hot tub, open-fireplace and separate treatment room on request. This chalet is perfect for families and groups!

Previously featured in Plate and Journey magazine and The Courier, chalet Fern Byre can be counted as one of only a handful of authentic farmhouses in the Chamonix valley available for rental. Located in the charming village of Les Houches, only minutes walk to the ski and mountain bike lifts, amenities, shops and several delightful restaurants and just a short drive from Chamonix town and the other ski/bike areas of the Chamonix valley.

The chalet is run as a luxury boutique hotel and is offered with total flexibility in mind. In winter the chalet provides luxury catered or self catered accommodation. In summer the chalet can be offered B&B or self catered. Our service can include in resort driving, airport transfers, and as experienced professionals with more than 27 yrs experience in Chamonix your holiday will be expertly delivered, whatever formula you choose!

Size Sleeps up to 11, 5 bedrooms
Nearest beach
Will consider Corporate bookings, House swap, Long term lets (over 1 month), Short breaks (1-4 days)
Access Car advised
Nearest Amenities 200 m
Nearest travel links Nearest airport: Geneva 100 km, Nearest railway: Les Houches 1 km
Family friendly Great for children of all ages, Suitable for people with restricted mobility
Notes Pets welcome, No smoking at this property
Features and Facilities

Luxuries Jacuzzi or hot tub, Sauna, Log fire, Internet access, DVD player
Pool Shared outdoor pool (unheated), Children's pool
General Central heating, TV, CD player, Table tennis, Safe, Satellite TV, Wi-Fi available
Standard Kettle, Toaster, Iron, Hair dryer
Utilities Clothes dryer, Dishwasher, Cooker, Microwave, Fridge, Freezer, Washing machine
Rooms 5 bedrooms, 5 bathrooms of which 5 En suites
Furniture Single beds (10), Cots (1), Dining seats for 12, Lounge seats for 12
Other High chair
Outdoors Shared outdoor pool (unheated), Balcony or terrace, Private garden, Shared garden, BBQ, Swing set
Access Parking
Further details indoors
With a myriad of chalets to choose from Chalet Fern Byre offers you something very special, the wonderful aimbience of a 230yr old Chamonix farmhouse married with modern, luxurious facilities. Owned and renovated by us over 5 years the Farm has been a labour of love..! but the attention to detail and quality of materials used has resulted in a very special property adored by all who stay.
Facilities include deep Italian leather sofa's juxtaposed with local mountain antiques and a modern granite and stainless steel kitchen married with hand-build cupboards. In the 5 bedrooms we have provided hotel standard zip-link beds so any room can be a double or a twin. We offer crisp, white, organic bed linen, goose feather duvets and leave you exclusive VOLA skincare bathroom products. The bathrooms are beautifully finished using Italian limestone tiles.
Wonderful valley views are framed from the huge picture windows, velux's and glass doors leading to the balcony. Our Eco features include geothermal generated underfloor heating, rain-water capture, clarivane double glazing, use of Dorvaplank, and re-use of the original wooden panels throughout providing a warm and indulgent ambience.
In the summer months we offer a private garden, ideal for al fresco dining plus the 'Swim-spa' hot tub provides a brilliant 'splash' pool for kids. We adorn the chalet with hanging baskets and can even offer a free minibus to Chamonix every morning for our B&B guests!
Chalet Fern Byre consists of the 2 upper floors of an ancient Alpine Farmhouse, with approximately 220 m2 of living space. The ground floor of the chalet is private (used by staff)
Further details outdoors
In Winter we provide bath-robes and crocs for the exterior 6m x 2.2m 'Swim Spa' hot tub, perfect for apres ski lounging!
In the summer months we offer a private side garden with BBQ, garden furniture, swings, table-tennis and the 'Swim-spa' hot tub provides a brilliant 'splash' pool for kids. We adorn the chalet with hanging baskets and the flower-covered balcony provides an ideal location for enjoying a cool drink and admiring the wonderful views.
Further details
Winter rentals are exclusive for groups. Rentals can be catered or self catered, for weeks or weekends, we are very flexible!
All Holidays can include our minibus service and airport transfers. Credit cards accepted.
Free concierge to book all ski packs, lessons or summer guides and mountain bikes.
Breakages deposit required for all rentals.
Summer holidays are self-catered or B&B.
Pressure washer available for mountian bikes.
The Rhone/French Alps region

The Mont Blanc massif offers an adrenalin packed holiday destination both winter and summer!

In winter you could ski 3 countries in one holiday! France, Switzerland and Italy! Boundless pistes and off piste variations including the famous 21km Combe Argentée trail (with a Guide)

In summer you can walk the 'Circuit des Crêtes Grises' and visit a host of charming villages and towns whilst admiring stunning Alpine pastures packed with the flora and fauna of the High Alps.

Locations worthy of a visit include Lake Annecy and the Old town of Annecy, the Pointe de Vorlan cable-car (Chamonix) for a wonderful view of the Alps and the Mont Blanc at 4807m (the highest mountain Peak in Europe). The Ice caves (accessed by the Belrioz railway) of the Combe Argentée are also worth a visit and for culture, Lyon, with its myriad of excellent shopping and restaurants and local exhibitions and museums.

Chamonix

Home to the sports of skiing and mountaineering, Chamonix is simply addictive. The dramatic mountains of the Chamonix valley incorporating the Mont Blanc Massif offers breathtaking scenery and make it a stunning setting for any skiing, snowboarding or summer activity holiday. With five separate ski areas scattered along the Chamonix valley, each with its own unique character and the famous off piste Combe Argentée run , every level of skier and snowboarder is amply catered for!

Les Houches is a pretty and unspoilt ski village which nestles just 5km from Chamonix town.

Les Houches is the largest single, pisted area in the Chamonix valley and has the added bonus of 86 snow canons covering 23 hectares of piste, this ski domain has wonderful skiing for beginners, intermediates and especially families.

The Chamonix valley has plenty to offer the non-skier, both rich in history and buzzing with shops, markets, bars, restaurants, exhibitions and festivals. There is also an seemingly unlimited variety of activities, from rock and ice climbing or snow shoe walking to x country and husky sledding. Chamonix is more than just a ski resort - it's a thriving mountain community, offering something for everyone. So join us this winter, you'll find our ski chalets simply gorgeous, our service attentive, our value for money excellent and your holiday experience simply unforgettable.

```html
<!DOCTYPE html>
<html lang="en">
<head>
<meta charset="utf-8">
<title>Timberline Haven</title>
<link href="https://fonts.googleapis.com/css2?family=Oswald:wght@300;400;500&family=Open+Sans:wght@400;600&display=swap" rel="stylesheet">
<style>
:root{
  --header:#2a1f1b;
  --wood-dark:#3a2f28;
  --gold:#f3b93a;
  --footer:#e2b33e;
  --footer-line:#b98a23;
  --caption-band:#433226;
  --ink:#2b211c;
  --muted:#5a514a;
  --white:#ffffff;
  --card:#e4e1dc;
}
*{margin:0;padding:0;box-sizing:border-box}
html,body{width:1200px;height:1200px;overflow:hidden}
body{position:relative;background:linear-gradient(90deg,#2f2620 0%,#5c4b3f 12%,#4a3b31 17%,#2e2620 100%);font-family:'Open Sans',sans-serif;color:var(--ink)}
.abs{position:absolute}
.site-header{left:0;top:0;width:1200px;height:104px;background:var(--header);border-bottom:1px solid #5a4a3e}
.brand{left:208px;top:38px;display:flex;align-items:center;gap:10px}
.brand-mark{width:14px;height:14px;background:var(--gold)}
.brand-name{font-family:'Oswald',sans-serif;font-weight:500;color:var(--gold);font-size:26px;line-height:30px}
.main-nav{right:208px;top:62px;display:flex;gap:30px;font-family:'Oswald',sans-serif;font-size:12.5px;color:#fff;letter-spacing:.3px}
.main-nav .active{color:var(--gold)}
.hero-photo{left:207px;top:105px;width:392px;height:339px;background:linear-gradient(135deg,#c9a36a,#8a5a2e 45%,#d8b27c 70%,#9a6c3d)}
.hero-offer{left:207px;top:358px;width:392px;text-align:right;padding-right:25px;color:var(--ink)}
.offer-name{font-size:14px}
.offer-price{font-size:20px;letter-spacing:1px;margin-top:-2px}
.offer-btn{display:inline-block;margin-top:2px;margin-right:8px;background:var(--gold);color:#5a3d10;font-family:'Oswald',sans-serif;font-size:12px;padding:3px 12px;border:1px solid #c58f1c;border-radius:2px}
.hero-copy{left:599px;top:105px;width:392px;height:339px;background:linear-gradient(180deg,#e9e4d8,#d9d3c4);padding:28px 25px 0 45px}
.hero-title{font-family:'Oswald',sans-serif;font-weight:400;font-size:33px;line-height:40px;text-align:center;color:var(--ink);margin-left:-20px}
.hero-text{margin-top:14px;font-size:11px;line-height:20px;text-align:justify;color:#3b332c}
.room{top:445px;width:261px}
.room-photo{height:150px}
.room-caption{height:84px;background:var(--caption-band);border-top:4px solid #8a6d3a;padding:11px 18px 0 18px}
.room-title{font-size:11px;color:var(--gold);font-weight:600}
.room-text{font-size:9.6px;line-height:15px;color:#fff;text-align:justify;margin-top:2px}
.info{left:207px;top:679px;width:784px;height:202px;background:var(--white)}
.label{font-family:'Oswald',sans-serif;font-weight:300;font-size:12px;color:var(--muted)}
.big{font-family:'Oswald',sans-serif;font-weight:400;font-size:22px;color:var(--ink);line-height:25px}
.dash-v{width:0;border-left:3px dotted #f0d57a}
.review{top:724px;width:224px;height:126px;background:var(--card)}
.review-text{padding:14px 0 0 13px;font-family:'Oswald',sans-serif;font-weight:300;font-size:11px;color:var(--ink)}
.review-name{font-size:12px;margin-top:14px;font-weight:400}
.review-more{margin-top:30px}
.review-photo{right:0;top:0;width:110px;height:126px;background:linear-gradient(160deg,#7a5a44,#b03a2a 55%,#5a3a2a)}
.site-footer{left:0;top:881px;width:1200px;height:319px;background:var(--footer)}
.f-head{font-family:'Oswald',sans-serif;font-size:13px;color:var(--ink)}
.f-small{font-family:'Oswald',sans-serif;font-weight:300;font-size:11px;color:var(--ink);line-height:15px}
.date-badge{width:32px;height:33px;background:var(--wood-dark);color:#fff;font-family:'Oswald',sans-serif;font-size:11px;text-align:center;line-height:14px;padding-top:3px;border-radius:2px}
.f-review{left:487px;width:228px}
.f-review .txt{position:absolute;left:42px;top:0;width:183px;text-align:justify;font-size:11.5px}
.dots-h{height:0;border-top:4px dotted var(--footer-line)}
.dots-v{width:0;border-left:3px dotted var(--footer-line)}
.email{left:753px;top:933px;width:238px;height:26px;border:2px solid #b98a23;background:#f2c64e;font-size:10px;padding:5px 9px;color:#5a4420}
.signup{left:753px;top:968px;width:69px;height:20px;background:var(--wood-dark);color:#fff;font-family:'Oswald',sans-serif;font-size:11px;text-align:center;line-height:20px;border-radius:2px}
.social{left:753px;top:1054px;display:flex;gap:14px;font-family:'Oswald',sans-serif;font-size:12px;color:var(--ink)}
.social span{display:flex;align-items:center;gap:5px}
.social i{display:inline-block;width:10px;height:10px;background:var(--ink)}
.copyright{left:208px;top:1179px;font-family:'Oswald',sans-serif;font-size:9px;letter-spacing:2px;color:#8a6a2a}
.foot-nav{right:209px;top:1179px;display:flex;gap:13px;font-family:'Oswald',sans-serif;font-size:9.5px;letter-spacing:1.5px;color:#8a6a2a}
</style>
</head>
<body>
<header class="site-header abs">
  <div class="brand abs">
    <span class="brand-mark"></span>
    <span class="brand-name">Timberline Haven</span>
  </div>
  <nav class="main-nav abs"><span class="active">HOME</span><span>ABOUT</span><span>GALLERY</span><span>CLIENT TESTIMONIAL</span><span>CONTACT</span></nav>
</header>

<div class="hero-photo abs" role="img" aria-label="Close-up of a wooden chair with a woven rush seat on a wooden floor"></div>
<div class="hero-offer abs">
  <div class="offer-name">Wooded House</div>
  <div class="offer-price">$250.00</div>
  <span class="offer-btn">VIEW DETAILS</span>
</div>
<section class="hero-copy abs">
  <h1 class="hero-title">High Quality<br>Wooden Used In It.<br>That’s Built to Last.</h1>
  <p class="hero-text">Exceptionally renovated Fern Byre dates from 1781 and offers the discerning skier a chance to stay in a wonderful mountain lodge. Spacious and light, there is a superb double aspect living and dining area and open-plan kitchen. All bedrooms are ensuite,and facilities include a sauna, enormous 6m ‘Swim spa’ hot tub, open-fireplace and separate treatment room on request. This chalet is perfect for families and groups!</p>
</section>

<article class="room abs" style="left:207px">
  <div class="room-photo" role="img" aria-label="Living room with light wooden floor and a sheepskin rug" style="background:linear-gradient(135deg,#d9a468,#a8703c 60%,#3a5a8a)"></div>
  <div class="room-caption"><div class="room-title">LIVING ROOM</div><p class="room-text">All livings room are ensuite, and facilities include a souna, enormous 6pm ‘Swim Spa’ hot tub, room on request.</p></div>
</article>
<article class="room abs" style="left:469px">
  <div class="room-photo" role="img" aria-label="Bedroom lounge with wood-panelled walls and a white sofa" style="background:linear-gradient(160deg,#c8c4bc,#b07a48 45%,#8a5a36)"></div>
  <div class="room-caption"><div class="room-title">BEDROOM</div><p class="room-text">All livings room are ensuite, and facilities include a souna, enormous 6pm ‘Swim Spa’ hot tub, room on request.</p></div>
</article>
<article class="room abs" style="left:731px;width:260px">
  <div class="room-photo" role="img" aria-label="Kitchen with wooden cabinets, island and bar stools" style="background:linear-gradient(180deg,#e6dccb,#9c7a55 55%,#c49a6a)"></div>
  <div class="room-caption"><div class="room-title">KITCHEN</div><p class="room-text">All livings room are ensuite, and facilities include a souna, enormous 6pm ‘Swim Spa’ hot tub, room on request.</p></div>
</article>

<section class="info abs">
  <div class="abs" style="left:18px;top:18px">
    <div class="label">FOR ORDER AND INQUIRIES PLEASE CALL:</div>
    <div class="big">555-014-8263</div>
    <div class="label" style="margin-top:34px">OR YOU CAN VISIT US AT:</div>
    <div class="big">4120 ALDER RIDGE ROAD<br>PINE HOLLOW, CO 80417</div>
  </div>
  <div class="dash-v abs" style="left:257px;top:6px;height:186px"></div>
  <div class="label abs" style="left:280px;top:18px">CLIENT TESTIMONIALS</div>
</section>
<div class="review abs" style="left:487px">
  <div class="review-text"><div>April 16, 2011</div><div class="review-name">Owen Carrick</div><div class="review-more">READ MORE</div></div>
  <div class="review-photo abs" role="img" aria-label="Craftsman in a plaid shirt working on a carving"></div>
</div>
<div class="review abs" style="left:747px">
  <div class="review-text"><div>April 16, 2011</div><div class="review-name">Dale Moreno</div><div class="review-more">READ MORE</div></div>
  <div class="review-photo abs" role="img" aria-label="Craftsman in a plaid shirt working on a carving"></div>
</div>

<footer class="site-footer abs">
  <div class="f-head abs" style="left:208px;top:25px">VISIT OUR CHALET</div>
  <div class="abs" role="img" aria-label="Modern chalet exterior with glass walls and a pool at dusk" style="left:208px;top:52px;width:241px;height:119px;background:linear-gradient(180deg,#e8e6e2,#c9a46a 55%,#3a3a3a)"></div>
  <div class="f-small abs" style="left:208px;top:183px">4120 ALDER RIDGE ROAD<br>PINE HOLLOW, CO 80417</div>
  <div class="f-small abs" style="left:208px;top:228px">555-014-8263</div>
  <div class="f-small abs" style="left:208px;top:258px;border-bottom:1px solid var(--ink)">stay@timberlinehaven.net</div>

  <div class="dots-v abs" style="left:465px;top:26px;height:244px"></div>
  <div class="f-head abs" style="left:487px;top:25px">RECENT CLIENT TESTIMONIALS</div>
  <div class="f-review abs" style="top:52px"><div class="date-badge">APR<br>16</div><div class="txt f-small"><div style="font-weight:400">Owen Carrick</div><div style="margin-top:4px">You gave us great services. We enjoyed alot. We recommend you to others.</div></div></div>
  <div class="f-review abs" style="top:127px"><div class="date-badge">APR<br>15</div><div class="txt f-small"><div style="font-weight:400">Dale Moreno</div><div style="margin-top:4px">You gave us great services. We enjoyed alot. We recommend you to others.</div></div></div>
  <div class="f-review abs" style="top:205px"><div class="date-badge">APR<br>14</div><div class="txt f-small"><div style="font-weight:400">Ian Ashby</div><div style="margin-top:4px">You gave us great services. We enjoyed alot. We recommend you to others.</div></div></div>
  <div class="dots-v abs" style="left:732px;top:26px;height:244px"></div>

  <div class="f-head abs" style="left:753px;top:25px">JOIN OUR NEWSLETTER</div>
  <div class="dots-h abs" style="left:753px;top:124px;width:238px"></div>
  <div class="f-head abs" style="left:753px;top:140px">SOCIAL MEDIA</div>
  <div class="dots-h abs" style="left:208px;top:281px;width:783px"></div>
</footer>
<div class="email abs">Enter Email Address Here For Updates</div>
<div class="signup abs">SIGN UP</div>
<div class="social abs"><span><i></i>Friendwall</span><span><i></i>Circlenet</span><span><i></i>Chirpline</span></div>
<div class="copyright abs">© 2013 TIMBERLINE HAVEN, ALL RIGHTS RESERVED</div>
<nav class="foot-nav abs"><span>HOME</span><span>ABOUT</span><span>GALLERY</span><span>BLOG</span><span>CONTACT</span></nav>
</body>
</html>
```